International Property Consultancy

Brief Overview:

I need a dynamic and well designed website that is easy to use and understand. It has to be unique and different to generic templates that most websites seem to be these days. PLEASE NO GENERIC TEMPLATES FROM THE INTERNET.

Our business has 10 years experience working on struggling international developments that we then work in-house for to turn around and brings bout success. We stay within a project often for long periods of time until success is achieved. We are unique in our approach and completely different to the standard routes to market for many developments. The site is for developers to see what we have done in regards to previous projects, as such we want to incorporate video into this site with a strong design aesthetic. There will be videos of the past projects we have worked on, which will act as case studies.

I like very simple but punchy websites, that people can navigate and understand very easily. Also a big fan of unique and well thought out design aesthetic.

Initial Site layout thoughts:

1) Homepage:
2) About Us
3) What we've done / Work
This part has the projects we have worked on (France, Portugal, London, Morocco). Each one will have some video content and photo images, but also would be good to have a succinct way to mention what we did and the successes in a clever and punchy way.

4) Contact Us

* This is just a guideline. Would be open to input and creative direction on your own part.

*More details and websites we like can be seen in the brief doc attached.

PLEASE VIEW THE WIREFRAME WORD DOC ATTACHED.

Here there are also some more examples to help:

Here are just a few examples of websites and what I like about them:

- www.velmoro.com (clean, nice geometric design aesthetic, good animation when loading and changing pages well thought out all though also coulee be considered a bit dull and basic after the initial homepage slide)
- https://www.farbridgehub.net (Clean site, quite clinical, lacks video content and doesn't engage greatly).
- https://ruskotile.com (minimal, and like how it mixes the design aesthetic more with video and photo content)

- https://www.amberquillworks.com (like the layout of this and how it displays the projects and work section)

- https://brisk.com (Good use of video content)

- https://loomfield.studio (minimal to the point and mixes design with video and animation etc...)

Here is another couple of cool websites that may help give you some direction: https://halvenquay.com www.brisk.com

Hi there, One of the things I thought would be good on the homepage is to add the logo with a 'digital landscape' before flicking down into a slide with video content of the projects... Just an idea but have posted some pics in the brief. We would get this animated for the site. But if you have better ideas, please do run with them. Thanks,

Target Market(s)

Property developers

Number of Pages Required

4 page

Font styles to use
Other font styles liked:
• Read brief

Requirements
Must have
• Needs to be clean, dynamic and easy to follow on desktop and mobile. We will use it as a kind of portfolio website so will need to embed video of past projects we have worked on.

Read brief in docs.
Nice to have
• Clean
Should not have
• Not be another generic template website.
Not have random property stock photos. (We are not a property agency).

```html
<!DOCTYPE html>
<html lang="en">
<head>
<meta charset="utf-8">
<title>Velantra — International Property Consultancy</title>
<link rel="stylesheet" href="https://fonts.googleapis.com/css2?family=Arimo:wght@400;700&family=Montserrat:wght@500;700;800&display=swap">
<style>
:root{
  --navy:#0f2a3a;
  --navy-deep:#0c1f2b;
  --navy-mid:#1c3f52;
  --ink:#1b1b1b;
  --muted:#8a8a8a;
  --white:#ffffff;
  --line:#c9c9c9;
}
*{margin:0;padding:0;box-sizing:border-box}
html,body{width:1200px;height:2637px;overflow:hidden;background:var(--white)}
body{position:relative;font-family:"Arimo",Arial,sans-serif;color:var(--ink)}
.abs{position:absolute}

/* header */
.site-header{position:absolute;left:0;top:0;width:1200px;height:85px;background:var(--white)}
.brand{position:absolute;font-family:"Montserrat",Arial,sans-serif;font-weight:500;letter-spacing:-0.5px}
.site-header .brand{left:104px;top:22px;font-size:38px;color:var(--ink)}
.main-nav{position:absolute;left:343px;top:36px;display:flex;gap:32px;font-size:16px}
.main-nav a{color:var(--ink);text-decoration:none}
.main-nav a.active{color:var(--navy-mid)}
.call{position:absolute;left:918px;top:22px}
.icon-circle{border-radius:50%;background:var(--navy);display:flex;align-items:center;justify-content:center}
.call .icon-circle{width:47px;height:47px}
.call-label{position:absolute;left:63px;top:0;font-size:15px;white-space:nowrap}
.call-number{position:absolute;left:63px;top:22px;font-size:19px;font-weight:700;color:var(--navy);white-space:nowrap}

/* hero */
.hero{position:absolute;left:0;top:85px;width:1200px;height:557px;
  background:linear-gradient(180deg,rgba(20,24,28,.25),rgba(20,24,28,.45)),
  linear-gradient(100deg,#5e5a55 0%,#8b8f92 25%,#b7bcbf 45%,#6f6a64 65%,#9a8f82 85%,#57504a 100%)}
.hero-title{position:absolute;left:0;width:1200px;top:182px;text-align:center;font-size:62px;font-weight:700;color:var(--white);letter-spacing:1px;text-shadow:0 2px 6px rgba(0,0,0,.4)}
.hero-sub{position:absolute;left:0;width:1200px;top:263px;text-align:center;font-size:26px;color:var(--white);text-shadow:0 1px 4px rgba(0,0,0,.4)}
.hero .play{left:560px;top:316px}
.dots{position:absolute;left:578px;top:519px;display:flex;gap:10px}
.dots span{width:8px;height:8px;border-radius:50%;background:var(--white)}

/* about */
.about-frame{position:absolute;left:108px;top:747px;width:274px;height:229px;border:8px solid var(--navy)}
.about-photo{position:absolute;left:144px;top:784px;width:340px;height:321px;background:linear-gradient(135deg,#d9dcdd 0%,#b9bec2 40%,#2e3d52 70%,#e6e8e8 100%)}
.about-title{position:absolute;left:526px;top:726px;font-size:41px;font-weight:700;color:var(--ink)}
.about-text{position:absolute;left:526px;top:795px;width:566px;font-size:16.5px;line-height:32.5px;text-align:justify;color:var(--ink)}
.btn{position:absolute;background:var(--navy);color:var(--white);font-weight:700;display:flex;align-items:center;justify-content:center;border-radius:3px}
.btn-read{left:523px;top:1107px;width:132px;height:48px;font-size:18px}

/* projects */
.projects{position:absolute;left:0;top:1231px;width:1200px;height:556px;background:linear-gradient(180deg,var(--navy-deep) 0%,#162f3e 60%,var(--navy-mid) 100%)}
.projects-title{position:absolute;left:0;width:1200px;top:46px;text-align:center;font-size:41px;font-weight:700;color:var(--white)}
.projects-sub{position:absolute;left:0;width:1200px;top:127px;text-align:center;font-size:18.5px;color:var(--white)}
.card{position:absolute;top:211px;width:273px}
.card-media{position:relative;width:273px;height:192px;border:2px solid #e9ecee;background:linear-gradient(135deg,#c9ced1,#6d7b86 55%,#3a4652)}
.card-brand{position:absolute;right:14px;top:12px;font-family:"Montserrat",Arial,sans-serif;font-weight:500;font-size:23px;color:var(--ink)}
.card-media .play{left:96px;top:56px}
.card-title{margin-top:26px;font-size:20px;font-weight:700;color:var(--white)}
.card-text{margin-top:8px;font-size:14px;font-weight:700;line-height:26px;color:var(--white)}

/* contact */
.section-heading{position:absolute;font-family:"Montserrat",Arial,sans-serif;font-weight:800;font-size:33px;color:var(--navy);letter-spacing:1px}
.contact-item{position:absolute;left:118px;display:flex;align-items:flex-start;gap:18px;font-size:21px;line-height:30px}
.contact-item .icon-circle{width:52px;height:52px;flex:none}
.field{position:absolute;border:2px solid #d6d6d6;border-radius:3px;box-shadow:0 1px 3px rgba(0,0,0,.15);font-size:16px;color:var(--muted);padding:20px 24px;letter-spacing:.5px}
.btn-submit{left:755px;top:2272px;width:132px;height:48px;font-size:19px;letter-spacing:1px}

/* footer */
.site-footer{position:absolute;left:0;top:2392px;width:1200px;height:245px;background:linear-gradient(180deg,var(--navy-deep),var(--navy-mid))}
.site-footer .brand{left:0;width:1200px;text-align:center;top:40px;font-size:41px;color:var(--white)}
.footer-nav{position:absolute;left:0;width:1200px;top:115px;display:flex;justify-content:center;gap:32px;font-size:16px}
.footer-nav a{color:var(--white);text-decoration:none}
.social{position:absolute;left:521px;top:162px;display:flex;gap:16px}
.social span{width:42px;height:42px;border-radius:50%;background:var(--white)}
</style>
</head>
<body>

<header class="site-header">
  <div class="brand">velantra.</div>
  <nav class="main-nav">
    <a class="active">HOME</a><a>ABOUT US</a><a>WHAT WE'VE DONE WORK</a><a>CONTACT US</a>
  </nav>
  <div class="call">
    <div class="icon-circle">
      <svg width="20" height="20" viewBox="0 0 24 24"><path fill="#fff" d="M6.6 10.8a15 15 0 0 0 6.6 6.6l2.2-2.2a1 1 0 0 1 1-.25 11.4 11.4 0 0 0 3.6.57 1 1 0 0 1 1 1V20a1 1 0 0 1-1 1A17 17 0 0 1 3 4a1 1 0 0 1 1-1h3.5a1 1 0 0 1 1 1c0 1.25.2 2.45.57 3.57a1 1 0 0 1-.25 1z"/></svg>
    </div>
    <div class="call-label">Call Us</div>
    <div class="call-number">555-014-2297</div>
  </div>
</header>

<section class="hero" role="img" aria-label="Team meeting around an office table">
  <h1 class="hero-title">VELANTRA</h1>
  <p class="hero-sub">Neque porro quisquam est qui dolorem ipsum quia .</p>
  <svg class="abs play" width="80" height="80" viewBox="0 0 80 80"><circle cx="40" cy="40" r="40" fill="rgba(255,255,255,.35)"/><circle cx="40" cy="40" r="31" fill="#0c1f2b"/><path d="M32 26 L55 40 L32 54 Z" fill="#fff"/></svg>
  <div class="dots"><span></span><span></span><span></span></div>
</section>

<div class="about-frame"></div>
<div class="about-photo" role="img" aria-label="Two colleagues reviewing documents at a desk"></div>
<h2 class="about-title">ABOUT US</h2>
<p class="about-text">Velantra is a consultancy company that helps international property developments fulfiltheir potential. The company has had great success over the last 10 years of turning aroundstruggling property developments (often resort and investment) and making them reach their maximum potential. We have completed projects in Portugal, London, France,Morocco, Brazil We work by white labelling or working in-house for each project creating a strategy that is bespoke and unique for each project. It allows a project to purely gain from any initiatives, i.e.. unlike paying agents to promote your project.</p>
<div class="btn btn-read">READ MORE</div>

<section class="projects">
  <h2 class="projects-title">OUR PROJECTS</h2>
  <p class="projects-sub">Neque porro quisquam est qui dolorem ipsum quia dolor sit amet, consectetur, adipisci velit.</p>

  <article class="card" style="left:32px">
    <div class="card-media" role="img" aria-label="Portugal Resort project video still">
      <span class="card-brand">velantra.</span>
      <svg class="abs play" width="72" height="72" viewBox="0 0 80 80"><circle cx="40" cy="40" r="40" fill="rgba(255,255,255,.35)"/><circle cx="40" cy="40" r="31" fill="#0c1f2b"/><path d="M32 26 L55 40 L32 54 Z" fill="#fff"/></svg>
    </div>
    <h3 class="card-title">Portugal Resort</h3>
    <p class="card-text">Neque porro quisquam est qui dolorem ipsum quia dolor sit amet.</p>
  </article>

  <article class="card" style="left:320px">
    <div class="card-media" role="img" aria-label="Morocco project video still">
      <span class="card-brand">velantra.</span>
      <svg class="abs play" width="72" height="72" viewBox="0 0 80 80"><circle cx="40" cy="40" r="40" fill="rgba(255,255,255,.35)"/><circle cx="40" cy="40" r="31" fill="#0c1f2b"/><path d="M32 26 L55 40 L32 54 Z" fill="#fff"/></svg>
    </div>
    <h3 class="card-title">Morocco</h3>
    <p class="card-text">Neque porro quisquam est qui dolorem ipsum quia dolor sit amet.</p>
  </article>

  <article class="card" style="left:606px">
    <div class="card-media" role="img" aria-label="London project video still">
      <span class="card-brand">velantra.</span>
      <svg class="abs play" width="72" height="72" viewBox="0 0 80 80"><circle cx="40" cy="40" r="40" fill="rgba(255,255,255,.35)"/><circle cx="40" cy="40" r="31" fill="#0c1f2b"/><path d="M32 26 L55 40 L32 54 Z" fill="#fff"/></svg>
    </div>
    <h3 class="card-title">London</h3>
    <p class="card-text">Neque porro quisquam est qui dolorem ipsum quia dolor sit amet.</p>
  </article>

  <article class="card" style="left:894px">
    <div class="card-media" role="img" aria-label="France project video still">
      <span class="card-brand">velantra.</span>
      <svg class="abs play" width="72" height="72" viewBox="0 0 80 80"><circle cx="40" cy="40" r="40" fill="rgba(255,255,255,.35)"/><circle cx="40" cy="40" r="31" fill="#0c1f2b"/><path d="M32 26 L55 40 L32 54 Z" fill="#fff"/></svg>
    </div>
    <h3 class="card-title">France</h3>
    <p class="card-text">Neque porro quisquam est qui dolorem ipsum quia dolor sit amet.</p>
  </article>
</section>

<h2 class="section-heading" style="left:118px;top:1903px">CONTACT US</h2>
<h2 class="section-heading" style="left:684px;top:1903px">GET IN TOUCH</h2>

<div class="contact-item" style="top:1987px">
  <div class="icon-circle"><svg width="26" height="20" viewBox="0 0 26 20"><rect x="1" y="1" width="24" height="18" rx="1" fill="none" stroke="#fff" stroke-width="2"/><path d="M1 2 L13 11 L25 2 M1 18 L10 9 M25 18 L16 9" fill="none" stroke="#fff" stroke-width="2"/></svg></div>
  <span style="padding-top:11px">info@velantra.com</span>
</div>
<div class="contact-item" style="top:2065px">
  <div class="icon-circle"><svg width="24" height="24" viewBox="0 0 24 24"><path fill="#fff" d="M6.6 10.8a15 15 0 0 0 6.6 6.6l2.2-2.2a1 1 0 0 1 1-.25 11.4 11.4 0 0 0 3.6.57 1 1 0 0 1 1 1V20a1 1 0 0 1-1 1A17 17 0 0 1 3 4a1 1 0 0 1 1-1h3.5a1 1 0 0 1 1 1c0 1.25.2 2.45.57 3.57a1 1 0 0 1-.25 1z"/></svg></div>
  <span style="padding-top:11px">Call: 555-014-2297</span>
</div>
<div class="contact-item" style="top:2147px">
  <div class="icon-circle"><svg width="22" height="28" viewBox="0 0 22 28"><path fill="#fff" d="M11 0A11 11 0 0 0 0 11c0 8 11 17 11 17s11-9 11-17A11 11 0 0 0 11 0zm0 16a5 5 0 1 1 0-10 5 5 0 0 1 0 10z"/></svg></div>
  <span>Neque porro quisquam est<br>qui dolorem ipsum quia<br>dolor sit amet,</span>
</div>

<div class="field" style="left:555px;top:1996px;width:251px;height:55px">First Name</div>
<div class="field" style="left:821px;top:1996px;width:252px;height:55px">Last Name</div>
<div class="field" style="left:555px;top:2066px;width:251px;height:54px">Phone</div>
<div class="field" style="left:821px;top:2066px;width:252px;height:54px">EMail</div>
<div class="field" style="left:555px;top:2138px;width:518px;height:100px">Message</div>
<div class="btn btn-submit">SUBMIT</div>

<footer class="site-footer">
  <div class="brand">velantra.</div>
  <nav class="footer-nav"><a>HOME</a><a>ABOUT US</a><a>WHAT WE'VE DONE WORK</a><a>CONTACT US</a></nav>
  <div class="social"><span aria-label="Social link"></span><span aria-label="Social link"></span><span aria-label="Social link"></span></div>
</footer>

</body>
</html>
```